Postcard Design

We are a yoga business that has a training called:
STEADY HARBOR-empowering educators and parents to give children and youth the gift of yoga and meditation as a tool for life. (We would like this description and the text below included in the postcard)

3-day training for educators and parents at our facility or yours.

You will leave equipped to teach mindful breathing techniques, meditation, and a yoga based sequence to revitalize the body. You will have the tools to empower your students to be confident and appreciate their mind-body connection.

**Training is designed for a minimum of 3 and a maximum of 15 educators and parents from the same organization.

FOR PRICING AND BOOKING :Jessa Corwin 555-273-6190
jcorwin@calmtidestudio.example

(Not to be included in design) We are using these postcards for a conference where teachers and school administrators go to find new things for their schools and students.
Updates

I thought I had uploaded our logo! so sorry but I made sure and saved it now I would like it on the design. Thank you.

Target Market(s)

Educators and parents of all age groups

Industry/Entity Type

Training

Font styles to use
Sans Serif

Requirements
Must have
• Pleas take out Bright Fennel logo (that is not our logo, but it is our picture and it is us in it) our logo is uploaded and we would like it to be used. Thank you.
Nice to have
• If possible use the pic I uploaded and take out the bright fennel logo and put STEADY HARBOR or our logo, also uploaded. This picture is of my son, husband, and I so we own it.
Should not have
• Corny yoga pictures or people dressed in all white.

```html
<!DOCTYPE html>
<html lang="en">
<head>
<meta charset="utf-8">
<title>Steady Harbor Postcard</title>
<link rel="stylesheet" href="https://fonts.googleapis.com/css2?family=Montserrat:wght@400;500;600&family=Questrial&display=swap">
<style>
  :root {
    --page: #ffffff;
    --forest-light: #6f9a3e;
    --forest-mid: #3f5f2a;
    --forest-deep: #1e2e17;
    --panel-shade: rgba(20, 28, 18, 0.45);
    --text-light: #f4f4f0;
    --ink: #1a1a1a;
    --navy: #2a2f5a;
    --rule: #9a9a9a;
    --card-shadow: 0 1px 4px rgba(0, 0, 0, 0.25);
  }
  * { margin: 0; padding: 0; box-sizing: border-box; }
  html, body { width: 1200px; height: 1000px; overflow: hidden; background: var(--page); }
  .canvas { position: relative; width: 1200px; height: 1000px; }

  .postcard {
    position: absolute; left: 326px; width: 544px; height: 422px;
    box-shadow: var(--card-shadow); overflow: hidden;
  }
  .postcard--front { top: 82px; }
  .postcard--back { top: 536px; background: var(--page); }

  .forest-photo {
    position: absolute; inset: 0;
    background:
      radial-gradient(ellipse at 50% 95%, var(--forest-light) 0%, transparent 55%),
      radial-gradient(ellipse at 15% 30%, #5d8a34 0%, transparent 45%),
      radial-gradient(ellipse at 88% 25%, #6c9a3a 0%, transparent 40%),
      linear-gradient(180deg, var(--forest-mid) 0%, var(--forest-deep) 55%, #3d5d22 100%);
  }
  .text-panel {
    position: absolute; left: 107px; top: 0; width: 333px; height: 100%;
    background: var(--panel-shade);
  }
  .front-copy {
    position: absolute; left: 107px; top: 0; width: 333px; height: 100%;
    color: var(--text-light); text-align: center;
    font-family: "Montserrat", sans-serif;
  }
  .brand-name {
    position: absolute; left: 0; right: 0;
    font-family: "Questrial", sans-serif; font-size: 15px; letter-spacing: 0.5px;
  }
  .front-copy .brand-name { top: 68px; color: var(--text-light); }
  .headline {
    position: absolute; left: 10px; right: 10px; top: 140px;
    font-size: 11px; font-weight: 600; letter-spacing: 0.9px; line-height: 14px;
  }
  .details {
    position: absolute; left: 14px; right: 14px; top: 178px;
    font-size: 7.4px; font-weight: 500; letter-spacing: 0.5px; line-height: 9.6px;
  }
  .details p + p { margin-top: 9px; }
  .booking {
    position: absolute; left: 0; right: 0; top: 276px;
    font-size: 9.2px; font-weight: 500; letter-spacing: 0.9px; line-height: 11.5px;
  }

  .back-brand {
    position: absolute; left: 20px; top: 62px; width: 96px;
    color: var(--navy); text-align: center; font-size: 14px; line-height: 16px;
  }
  .back-contact {
    position: absolute; left: 36px; top: 303px;
    font-family: "Questrial", sans-serif; font-size: 13px; letter-spacing: 0.8px; line-height: 15px;
    color: var(--ink);
  }
  .divider { position: absolute; left: 261px; top: 139px; width: 2px; height: 210px; background: var(--rule); }
  .address-lines { position: absolute; left: 288px; top: 219px; width: 212px; }
  .address-lines span { display: block; height: 2px; background: var(--rule); margin-bottom: 20.5px; }
  .mission {
    position: absolute; left: 25px; right: 40px; top: 377px;
    font-family: "Montserrat", sans-serif; font-size: 8.6px; line-height: 11.5px; color: var(--ink);
  }
</style>
</head>
<body>
<main class="canvas">
  <section class="postcard postcard--front">
    <div class="forest-photo" role="img" aria-label="Mossy old-growth forest photo with three family members in yoga poses: a woman in tree pose at left, a seated child at center, a man in tree pose at right"></div>
    <div class="text-panel"></div>
    <div class="front-copy">
      <div class="brand-name">Calm Tide Studio</div>
      <h1 class="headline">3-day training for educators and parents at our facility or yours.</h1>
      <div class="details">
        <p>You will leave equipped to teach mindful breathing techniques, meditation, and a yoga based sequence to revitalize the body. You will have the tools to empower your students to be confident and appreciate their mind-body connection.</p>
        <p>**Training is designed for a minimum of 3 and a maximum of 15 educators and parents from the same organization.</p>
      </div>
      <div class="booking">
        FOR PRICING AND BOOKING :<br>
        Jessa Corwin 555-273-6190<br>
        jcorwin@calmtidestudio.example
      </div>
    </div>
  </section>

  <section class="postcard postcard--back">
    <div class="brand-name back-brand">Calm Tide Studio</div>
    <div class="back-contact">
      Jessa Corwin 555-273-6190<br>
      jcorwin@calmtidestudio.example
    </div>
    <div class="divider"></div>
    <div class="address-lines"><span></span><span></span><span></span><span></span></div>
    <p class="mission">STEADY HARBOR-empowering educators and parents to give children and youth the gift of yoga and meditation as a tool for life.</p>
  </section>
</main>
</body>
</html>
```